The WILLOW Lodge is a transitional living housue for women in recovery. It is structured and loving an

I have uploaded my old brochure which was not designed professionally. I want a fresh, funky feel. Our website is www.willowlodgeofthecedarshores.com if you want to get ideas from that but I do not like the bubbles on it. I have uploded a few pics of the houses and the backyards. Please help us convey love and hope and recovery!

```html
<!DOCTYPE html>
<html lang="en">
<head>
<meta charset="utf-8">
<title>WILLOW Lodge Brochure</title>
<link href="https://fonts.googleapis.com/css2?family=Questrial&family=Mystery+Quest&family=Della+Respira&display=swap" rel="stylesheet">
<style>
:root{
  --purple:#6f4aa0;
  --leaf:#8bbf3f;
  --leaf-light:#c4e08a;
  --leaf-deep:#6e9a2c;
  --sage:#5e8c6c;
  --ink:#2b2b2b;
  --ink-soft:#3e3e3e;
  --white:#ffffff;
  --mint:#a5d56a;
}
*{margin:0;padding:0;box-sizing:border-box}
html,body{width:1200px;height:1145px;overflow:hidden;background:var(--white)}
body{position:relative;font-family:"Questrial",sans-serif;color:var(--ink)}
.brochure{position:absolute;left:333px;top:31px;width:780px;height:1108px}
.panel{position:absolute;width:260px;height:554px;overflow:hidden}
.panel .photo{position:absolute;inset:0}
.panel .content{position:absolute;inset:0}
.row-top{top:0;height:553px}
.row-bottom{top:553px;height:555px}
.col-1{left:0}.col-2{left:260px}.col-3{left:520px}

.script-head{font-family:"Mystery Quest",cursive;color:var(--purple);font-weight:400}
.serif-head{font-family:"Della Respira",serif;font-weight:400}
.body-copy{font-size:9.3px;line-height:15.9px;letter-spacing:.06em}

/* Sisters & Supports */
.sisters .photo{background:linear-gradient(170deg,#e9efe6 0%,#d5dccd 40%,#c9c9bd 70%,#d8d7cd 100%)}
.sisters h2{position:absolute;left:20px;top:26px;font-size:19px;letter-spacing:.02em}
.sisters .body-copy{position:absolute;left:17px;top:78px;width:198px;color:var(--ink-soft)}
.sisters .nearby{position:absolute;left:12px;right:12px;top:457px;text-align:center;font-size:9.3px;line-height:16.5px;font-weight:700;letter-spacing:.08em;color:var(--sage)}

/* Treatment */
.treatment .photo{background:linear-gradient(90deg,#dcdcda,#ecebe8 30%,#dedddb 60%,#e9e8e5)}
.treatment h2{position:absolute;left:0;right:0;top:18px;text-align:center;font-size:14.5px;line-height:21px;letter-spacing:.04em}
.treatment .card{position:absolute;left:18px;top:80px;width:233px;height:322px;background:rgba(255,255,255,.72);padding:19px 8px 0 8px;font-size:9.3px;line-height:15.9px;letter-spacing:.06em;color:var(--ink)}
.treatment ol{list-style:none;margin-bottom:14px}
.treatment .card p{color:var(--ink-soft)}
.treatment .card strong{font-weight:400;color:var(--ink);display:block}
.treatment ul{list-style:none;font-size:8.2px;line-height:12.9px;margin-top:1px}
.treatment ul li::before{content:"• "}
.signoff{position:absolute;left:30px;right:30px;top:413px;text-align:center}
.region{font-family:"Mystery Quest",cursive;color:var(--leaf-deep);letter-spacing:.28em}
.signoff .region{font-size:12px}
.signoff .tag{font-size:7px;letter-spacing:.12em;color:var(--ink-soft)}
.signoff .rule{height:1px;background:var(--leaf);margin:4px 0 0}
.signoff .mark{display:flex;align-items:center;justify-content:center;gap:5px;margin-top:15px;font-size:9.5px;letter-spacing:.08em;color:var(--ink-soft)}
.signoff .mark span.dot{width:8px;height:8px;border-radius:50%;background:var(--leaf)}
.signoff .lines{margin-top:16px;font-size:7.6px;line-height:16px;letter-spacing:.14em;color:var(--ink-soft)}

/* Cover */
.cover .photo{background:linear-gradient(180deg,#a9c98a 0%,#b7d29e 25%,#c3d7ad 55%,#b8cfa0 80%,#a9c795 100%)}
.cover .band{position:absolute;left:0;top:0;width:100%;height:51px;background:rgba(214,236,170,.9);text-align:center;padding-top:5px}
.cover .band .region{font-size:19.5px;letter-spacing:.2em}
.cover .band .tag{font-size:10.5px;letter-spacing:.16em;color:#667a52;margin-top:2px}
.cover .namebox{position:absolute;left:52px;top:148px;width:159px;height:75px;background:var(--mint);text-align:center;padding-top:15px;color:#567c2a}
.cover .namebox .big{font-family:"Della Respira",serif;font-size:21px}
.cover .namebox .small{font-family:"Della Respira",serif;font-size:10.5px;margin-top:3px}
.cover .contact{position:absolute;left:27px;top:432px;width:206px;height:71px;background:rgba(255,255,255,.2);text-align:center;padding-top:10px;font-size:8.4px;line-height:18px;letter-spacing:.1em;color:rgba(255,255,255,.85)}
.cover .contact .url{font-size:7.6px}

/* Living in Recovery */
.living .photo{background:linear-gradient(180deg,#6b6796 0%,#6d6b98 40%,#7a7ea3 70%,#8089a6 100%)}
.living h2{position:absolute;left:0;right:0;top:22px;text-align:center;font-size:18px;color:#3a2d50;letter-spacing:.04em}
.living .body-copy{position:absolute;left:26px;right:24px;top:65px;text-align:center;color:rgba(255,255,255,.92);font-size:9.6px;line-height:14.4px;letter-spacing:.09em}
.living .badge{position:absolute;left:168px;top:465px;width:80px;height:81px}

/* Overview */
.overview .photo{background:linear-gradient(180deg,#5a6e5a 0%,#6e8a6c 35%,#86a79b 60%,#5fa4b4 80%,#4fa7ba 100%)}
.overview h2{position:absolute;left:0;right:0;top:22px;text-align:center;font-size:19px;color:#2a2a2a}
.overview .list{position:absolute;left:24px;right:24px;top:66px}
.overview h3{font-family:"Della Respira",serif;font-weight:400;font-size:10px;color:#263126;line-height:13px}
.overview p{font-size:8.4px;line-height:13.5px;letter-spacing:.08em;color:rgba(255,255,255,.9);margin-bottom:1px}

/* Services */
.services .photo{background:linear-gradient(180deg,#4f5e52 0%,#5a6b5d 40%,#616e66 70%,#56615b 100%)}
.services .list{position:absolute;left:21px;right:20px;top:16px}
.services h3{font-family:"Della Respira",serif;font-weight:400;font-size:10px;color:var(--leaf);line-height:14px;margin-top:2px}
.services p{font-size:8.4px;line-height:13.5px;letter-spacing:.08em;color:rgba(255,255,255,.92);margin-bottom:2px}
.services .closing{position:absolute;left:20px;right:20px;top:465px;border-top:1px solid rgba(255,255,255,.3);text-align:center;padding-top:8px;font-family:"Della Respira",serif;color:var(--white);font-size:11.5px;line-height:26px;letter-spacing:.14em}
</style>
</head>
<body>
<div class="brochure">

  <section class="panel row-top col-1 sisters">
    <div class="photo" role="img" aria-label="Photo of a wooden boardwalk winding through lush green trees"></div>
    <div class="content">
      <h2 class="script-head">Sisters &amp; Supports</h2>
      <p class="body-copy">The WILLOW Lodge is known for creating an instant support system for those in early recovery. We have developed a FREEDOM house to offer our recovering sisters after they have completed their goals at the WILLOW Lodge. It's a self-managed home with a lower rent, designed for women to save money and practice living on their own! We reinforce the benefits of healthy interdependency upon women in recovery and offer beautiful, serene, and safe housing for women to live and visit. No one ever has to be alone during early recovery.</p>
      <p class="nearby">We are located close to south Florida beaches, parks, churches, shopping and schools.</p>
    </div>
  </section>

  <section class="panel row-top col-2 treatment">
    <div class="photo" role="img" aria-label="Soft whitewashed wood grain texture"></div>
    <div class="content">
      <h2 class="script-head">We recognize the multiple<br>benefits of treatment programs:</h2>
      <div class="card">
        <ol>
          <li>1) professional case management</li>
          <li>2) individual therapy</li>
          <li>3) group therapy and</li>
          <li>4) education.</li>
        </ol>
        <p>Once determined a woman is a proper fit for one of our houses, we are committed to reinforcing the individualized plan recommended by her treatment center and will work in conjunction with the center's staff.</p>
        <strong>We offer additional guidance on an individual basis which may include:</strong>
        <ul>
          <li>Relapse Prevention</li>
          <li>Financial management/budgeting</li>
          <li>Resume writing &amp; Job coaching</li>
          <li>Case management</li>
          <li>Medication monitoring</li>
          <li>Recovery coaching</li>
        </ul>
      </div>
      <div class="signoff">
        <div class="region">South Florida</div>
        <div class="tag">Recovery Homes for Women</div>
        <div class="rule"></div>
        <div class="mark"><span class="dot"></span>Willow Lodge</div>
        <div class="lines">Willow Lodge of the Cedar Shores<br>Marlow Bay, FL<br>(555) 314-0728<br>www.willowlodgeofthecedarshores.com</div>
      </div>
    </div>
  </section>

  <section class="panel row-top col-3 cover">
    <div class="photo" role="img" aria-label="Photo of a small house with a front door and white picket fence under a tree, tinted green"></div>
    <div class="content">
      <div class="band">
        <div class="region">South Florida</div>
        <div class="tag">Recovery Homes for Women</div>
      </div>
      <div class="namebox">
        <div class="big">Willow Lodge</div>
        <div class="small">of the Cedar Shores</div>
      </div>
      <div class="contact">Marlow Bay, FL<br>(555) 314-0728<br><span class="url">www.willowlodgeofthecedarshores.com</span></div>
    </div>
  </section>

  <section class="panel row-bottom col-1 living">
    <div class="photo" role="img" aria-label="Photo of a garden pond with lily pads, tinted purple"></div>
    <div class="content">
      <h2 class="serif-head">Living in Recovery</h2>
      <p class="body-copy">The WILLOW Lodge was created to offer women a place to practice using their newly acquired sober living skills within the safety of a managed, independent living environment. We guide women into their foundation of a twelve step program and rein force the necessity of the life saving tools.<br>We encourage women to incorporate the spiritual principles of the twelve steps into all of her affairs. This gives women a chance to become strong in her recovery before returning home or embarking on a new adult life.<br>The communities are beautiful and serene. While we teach discipline, life skills, and work habits, we also teach the values of honesty, worthiness, and self-esteem. We provide comfortable and aesthetically appealing homes of which the women are proud to be a part.</p>
      <svg class="badge" viewBox="0 0 80 81" aria-hidden="true">
        <rect width="80" height="40" fill="#5a3a8c"/>
        <rect y="40" width="80" height="41" fill="#5fc6cf"/>
      </svg>
    </div>
  </section>

  <section class="panel row-bottom col-2 overview">
    <div class="photo" role="img" aria-label="Photo of a backyard swimming pool surrounded by palms and patio chairs"></div>
    <div class="content">
      <h2 class="serif-head">Overview</h2>
      <div class="list">
        <h3>Living Skills</h3>
        <p>We hold a mandatory weekly living skills meeting where house issues are solved. We learn in recovery that basic living skills are a necessary discipline, help build self-esteem, and help us learn accountability.</p>
        <h3>Relapse Prevention</h3>
        <p>We offer a mandatory weekly relapse prevention group. Alumni are encouraged to continue this group after they have left the house.</p>
        <h3>Group Activities</h3>
        <p>We encourage women to get involved with the sober communities by participating and/or serving in organized events.</p>
        <h3>Resource Center</h3>
        <p>We offer a house computer, phone and internet access. We also have resume writing software and computer software tutorials for those new to computers or rusty in old skills.</p>
        <h3>Location</h3>
        <p>Residences are closely located to recovery club houses and many church meetings. Additionally, there is easy access to public transportation.</p>
        <h3>Healthcare &amp; Healing</h3>
        <p>Healthcare &amp; Healing<br>We have developed a network of reputable healing specialists in the areas to meet individual needs.</p>
      </div>
    </div>
  </section>

  <section class="panel row-bottom col-3 services">
    <div class="photo" role="img" aria-label="Photo of tall palms and tropical plants beside the pool, darkened"></div>
    <div class="content">
      <div class="list">
        <h3>Social Services</h3>
        <p>Managers have thorough knowledge of social services in local areas. Some women may be eligible for assistance.</p>
        <h3>In-house managers</h3>
        <p>Property Managers are in recovery. They also have experience in many areas of addiction related problems and remain mindful of issues that may arise during this time. Managers address the issues efficiently and with the appropriate people.</p>
        <h3>Senior Sister System</h3>
        <p>We encourage the women with more clean time to take on a lead position of responsibility in the houses. It enables women to be accountable to one another and not just authority figures.</p>
        <h3>Mind, Body, &amp; Spirit</h3>
        <p>Living clean and sober is a process. We encourage healing on all levels.</p>
        <h3>Your Responsibility</h3>
        <p>You are responsible for making a decision to stay clean and sober, packing a bag, and moving in! We supply linens, towels, cleaning and paper products.</p>
      </div>
      <div class="closing">WILLOW Lodge of the Cedar<br>Shores<br>(555) 314-0728</div>
    </div>
  </section>

</div>
</body>
</html>
```